Belmora Wines

Hi all,

My name’s Tom Welling and I run a small wine brand based in the Canberra Wine District, Australia. I’m currently in the process of branding the business and am looking for a designer to help develop a new visual direction.

Background
I’ll be growing my own fruit from a leased vineyard site Named 'Kestrove' and my family’s property named 'Tallin Park', with a stronger emphasis on organic practices and site expression.

The Direction
The brand will centre around single vineyard wines, with each wine reflecting the unique site it comes from. I’d like the branding to support this idea of place, origin, and authenticity.

In terms of visual style, I’m drawn to something that is:

Simple and effective
A balance between traditional and modern
Clean, considered, and not overly decorative

Nothing too over-the-top, the goal is something timeless that lets the wine and vineyard story speak for itself.

At this stage, I’m mainly looking for:

Conceptual design direction / ideas
Label design (with potential to expand into broader branding)

I’m open to creative interpretation, so if the story resonates with you, I’d love to see how you would approach it.

Below I've attached an example of the bottle shape I will be using.

Cheers,
Tom

Colors
0054AA
0677BA
7BADD7
CADEEF
E8F1F8
FFC000
F8CF3A
FAE287
FDF2CF
FEFAEE

Requirements
Must have
• Mix of modern and traditional

```html
<!DOCTYPE html>
<html lang="en">
<head>
<meta charset="utf-8">
<title>Kestrove Chardonnay Label</title>
<link rel="stylesheet" href="https://fonts.googleapis.com/css2?family=Inter:wght@300;400&display=swap">
<style>
  :root {
    --canvas: #ffffff;
    --vine-green: #7a8c21;
    --earth-brown: #764100;
    --chalk: #f1f3ea;
  }
  html, body {
    margin: 0;
    padding: 0;
    width: 1200px;
    height: 1000px;
    overflow: hidden;
    background: var(--canvas);
  }
  .stage {
    display: block;
    width: 1200px;
    height: 1000px;
  }
  .label-sky { fill: var(--vine-green); }
  .label-hill { fill: var(--earth-brown); }
  .bird-mark { fill: var(--chalk); opacity: 0.9; }
  .vineyard-name {
    font-family: "Inter", "Helvetica Neue", Arial, sans-serif;
    font-weight: 300;
    font-size: 104px;
    fill: var(--chalk);
  }
  .varietal {
    font-family: "Inter", "Helvetica Neue", Arial, sans-serif;
    font-weight: 300;
    font-size: 23px;
    fill: var(--vine-green);
  }
</style>
</head>
<body>
<svg class="stage" viewBox="0 0 1200 1000" xmlns="http://www.w3.org/2000/svg">
  <g class="wine-label" transform="translate(424 256)">
    <rect class="label-sky" x="0" y="0" width="346" height="481"/>
    <path class="label-hill" d="M0 322 C 70 262, 170 240, 250 244 C 300 246, 330 250, 346 256 L346 481 L0 481 Z"/>
    <rect class="bird-mark" x="46" y="60" width="68" height="62" rx="6" role="img" aria-label="Small swallow illustration in flight"/>
  </g>
  <text class="vineyard-name" x="0" y="0" transform="translate(716 685) rotate(-90)" textLength="385" lengthAdjust="spacing">kestrove</text>
  <text class="varietal" x="450" y="713" textLength="130" lengthAdjust="spacingAndGlyphs">chardonnay</text>
</svg>
</body>
</html>
```